Flyer Design for Upcoming Baseball Clinics, Camps, and Academies

What We Need:
We are looking for a design template we can use for our upcoming sports camps, clinics, and academies. We do elite level training with youth to professional athletes and brand awareness is our number one concern right now.

Ideally this template can be used across multiple sports. Here is our premise:

Clinics (1-Day Event to attract 50+ Athletes)
Camps (2-4 Day Events looking to attract 100+)
Academies (More intimate and skill specific. lasts 6-8 weeks. 10-20 athletes)

Our plan is to do this for Baseball, Football, Basketball, and Lacrosse.

The ideal situation is to be able to use this as a template so we can just edit the document in the future.

Target Market(s)

Prep: Middle School Athletes / ELITE: High School Athletes

Industry/Entity Type

Training

Requirements
Must have
• Things to include:
• Logo, Dates, Times, Investment, Description, Benefits, our mission statement, etc. Our specific colors, specific font family (Bunken Tech Sans Wide), follow our branding deck which is attached.
• Info:
• K7Z BASEBALL CLINIC
• Date: November 11th, 2017
• AGES: PREP: (5th to 8th Grade). ELITE (9th-12th Grade)
• Registration: 8:00am - 9:00 am / 11:00 am - Noon
• Times:
• PREP: 9:00am - 11:00 am
• ELITE: Noon - 2pm
• Investment: $199
• Current Members: $99
Nice to have
• It would be nice to see our mission statement tied in somehow in a unique way. Also maybe a testimonial or two from our pro athletes??
Should not have
• Fake Images: Any Image used needs to be real and give off an authentic feel of a baseball player and the culture.

```html
<!DOCTYPE html>
<html lang="en">
<head>
<meta charset="utf-8">
<title>K7Z Baseball Clinic Flyer</title>
<link rel="stylesheet" href="https://fonts.googleapis.com/css2?family=Saira:wdth,wght@50..125,100..900&display=swap">
<style>
  :root {
    --mat: #808184;
    --teal: #178ea0;
    --charcoal: #3c4144;
    --black: #0a0a0a;
    --white: #ffffff;
    --ink: #3a3f42;
    --photo-field: #5b6f63;
    --photo-lax: #5f8a3c;
    --photo-dirt: #8a4a32;
  }
  * { margin: 0; padding: 0; box-sizing: border-box; }
  html, body { width: 908px; height: 1200px; overflow: hidden; background: var(--mat); }
  body { font-family: "Saira", "Arial", sans-serif; font-stretch: 125%; }
  .flyer { position: absolute; left: 40px; top: 64px; width: 828px; height: 1072px; background: var(--white); overflow: hidden; }
  .layer { position: absolute; left: 0; top: 0; }
  .brand { position: absolute; left: 55px; top: 300px; width: 150px; text-align: center; color: var(--white); font-weight: 700; font-size: 44px; letter-spacing: 2px; }
  .mission { position: absolute; left: 0; top: 426px; width: 828px; height: 100px; text-align: center; color: var(--white); }
  .mission-label { position: absolute; top: 14px; width: 100%; font-weight: 800; font-size: 14px; letter-spacing: 1px; }
  .mission-lead { position: absolute; top: 34px; width: 100%; font-weight: 600; font-size: 16px; letter-spacing: 1px; }
  .mission-focus { position: absolute; top: 56px; width: 100%; font-weight: 700; font-size: 29px; letter-spacing: 2px; }
  .statement { position: absolute; top: 546px; width: 828px; text-align: center; color: var(--ink); font-weight: 700; font-size: 27px; line-height: 38px; letter-spacing: 1px; }
  .programs { position: absolute; top: 684px; left: 0; width: 828px; display: flex; }
  .program { width: 276px; text-align: center; color: var(--ink); }
  .program h2 { color: var(--teal); font-weight: 600; font-size: 20px; letter-spacing: 1px; margin-top: 8px; margin-bottom: 8px; }
  .program p { font-size: 13px; line-height: 18px; font-weight: 500; letter-spacing: .5px; padding: 0 30px; }
  .event-title { position: absolute; top: 810px; width: 828px; text-align: center; color: var(--white); font-weight: 800; font-size: 35px; letter-spacing: 2px; }
  .event-date { position: absolute; top: 860px; width: 828px; text-align: center; color: var(--white); font-weight: 600; font-size: 16px; letter-spacing: 1px; }
  .details { position: absolute; top: 902px; color: var(--white); font-weight: 600; font-size: 17px; line-height: 22px; letter-spacing: 1px; }
  .details p + p { margin-top: 21px; }
  .details-left { left: 43px; }
  .details-right { left: 510px; }
</style>
</head>
<body>
<main class="flyer">
  <svg class="layer" width="828" height="1072" viewBox="0 0 828 1072" aria-hidden="false">
    <!-- Photo row -->
    <polygon points="0,0 309,0 273,426 0,426" fill="var(--photo-field)" role="img" aria-label="Photo: baseball players running sprint drills on a field"/>
    <polygon points="313,0 590,0 522,426 277,426" fill="var(--photo-lax)" role="img" aria-label="Photo: lacrosse player running with stick at a tournament"/>
    <polygon points="594,0 828,0 828,426 526,426" fill="var(--photo-dirt)" role="img" aria-label="Photo: softball player sliding on the infield dirt"/>
    <!-- Mission band -->
    <rect x="0" y="426" width="828" height="100" fill="var(--charcoal)"/>
    <polygon points="101,426 758,426 731,526 69,526" fill="var(--teal)"/>
    <polygon points="97,426 101,426 69,526 65,526" fill="var(--white)"/>
    <polygon points="758,426 762,426 735,526 731,526" fill="var(--white)"/>
    <!-- Program dividers -->
    <rect x="267" y="684" width="3" height="105" fill="var(--teal)"/>
    <rect x="537" y="684" width="3" height="105" fill="var(--teal)"/>
    <!-- Event band -->
    <rect x="0" y="796" width="828" height="100" fill="var(--black)"/>
    <polygon points="96,796 758,796 731,896 69,896" fill="var(--charcoal)"/>
    <polygon points="99,796 104,796 75,896 70,896" fill="var(--teal)"/>
    <polygon points="758,796 763,796 734,896 729,896" fill="var(--teal)"/>
    <!-- Details panel -->
    <rect x="0" y="896" width="828" height="176" fill="var(--teal)"/>
    <polygon points="477,896 481,896 461,1072 457,1072" fill="var(--white)"/>
  </svg>

  <div class="brand">K7Z</div>

  <section class="mission">
    <p class="mission-label">OUR MISSION</p>
    <p class="mission-lead">TO TRAIN, INSTRUCT, MOTIVATE &amp; EMPOWER</p>
    <p class="mission-focus">THE ATHLETE INSIDE YOU</p>
  </section>

  <p class="statement">We do elite level training with youth to<br>professional athletes &amp; brand awareness<br>is our number one concern right now</p>

  <section class="programs">
    <div class="program"><h2>CLINICS</h2><p>(1-Day Event to attract 50+ Athletes)</p></div>
    <div class="program"><h2>CAMPS</h2><p>(2-4 Day Events looking to attract 100+)</p></div>
    <div class="program"><h2>ACADEMIES</h2><p>(More intimate and skill specific. lasts 6-8 weeks. 10-20 athletes)</p></div>
  </section>

  <h1 class="event-title">K7Z BASEBALL CLINIC</h1>
  <p class="event-date">Date: November 11th, 2017</p>

  <section class="details details-left">
    <p>AGES:<br>PREP: (5th to 8th Grade).<br>ELITE (9th-12th Grade)</p>
    <p>Registration:<br>8:00am - 9:00 am / 11:00 am - Noon</p>
  </section>
  <section class="details details-right">
    <p>Times:<br>PREP: 9:00am - 11:00 am<br>ELITE: Noon - 2pm</p>
    <p>Investment: $199<br>Current Members: $99</p>
  </section>
</main>
</body>
</html>
```